Remodeling brochure

We need an informative homeowner friendly brochure detailing our company and things we do. We are looking for an initial setup and ideas (# of pages, etc) and then we will send more content. We are uploading our logo design. We are a high end remodeling company specializing in kitchen & bath remodels. We sell ourselves on customer communication and attention to detail in our designs and remodels.

Target Market(s)

Residential homeowners

Contact Information for Business Card

Modern and attention grabbing

Requirements
Must have
• Name- Hearth & Tile Crafters<br/>Address- 728 NW Folley Lane Suite #217<br/> Marlow Springs, Ohio 50388<br/>Phone- 555-472-8093<br/>email-htcrafterspro@mailvane.net

```html
<!DOCTYPE html>
<html lang="en">
<head>
<meta charset="utf-8">
<title>Hearth &amp; Tile Crafters – Pocket Folder</title>
<link href="https://fonts.googleapis.com/css2?family=Source+Sans+3:wght@400;600&display=swap" rel="stylesheet">
<style>
  :root {
    --stage: #c3c3c3;
    --blue-light: #1f97d7;
    --blue-mid: #1c78c0;
    --blue-deep: #2a44a0;
    --paper: #ffffff;
    --fold-line: #d8dbe6;
  }
  html, body {
    margin: 0;
    padding: 0;
    width: 1200px;
    height: 1032px;
    overflow: hidden;
    background: var(--stage);
  }
  .folder {
    display: block;
    width: 1200px;
    height: 1032px;
    font-family: "Source Sans 3", "Myriad Pro", sans-serif;
  }
  .grad-top { stop-color: var(--blue-light); }
  .grad-mid { stop-color: var(--blue-mid); }
  .grad-bottom { stop-color: var(--blue-deep); }
  .paper { fill: var(--paper); }
  .photo-kitchen { fill: url(#kitchenTone); }
  .photo-bath { fill: url(#bathTone); }
  .fold { stroke: var(--fold-line); stroke-width: 0.6; }
  .brand-name { fill: var(--blue-mid); font-size: 21px; font-weight: 600; }
  .brand-mark { fill: var(--blue-mid); }
  .back-name { fill: var(--paper); font-size: 22px; font-weight: 600; }
  .address, .contact, .web { fill: var(--paper); font-weight: 400; }
  .address { font-size: 9.8px; }
  .contact { font-size: 9.6px; }
  .web { font-size: 11px; letter-spacing: 0.2px; }
  .icon { fill: none; stroke: var(--paper); stroke-width: 1; }
  .icon-fill { fill: var(--paper); }
</style>
</head>
<body>
<svg class="folder" viewBox="0 0 1200 1032" xmlns="http://www.w3.org/2000/svg">
  <defs>
    <linearGradient id="blueFade" x1="0" y1="0" x2="0" y2="1">
      <stop offset="0" class="grad-top"/>
      <stop offset="0.4" class="grad-mid"/>
      <stop offset="1" class="grad-bottom"/>
    </linearGradient>
    <linearGradient id="flapFade" x1="0" y1="0" x2="0" y2="1">
      <stop offset="0" class="grad-bottom"/>
      <stop offset="0.5" class="grad-mid"/>
      <stop offset="1" class="grad-top"/>
    </linearGradient>
    <linearGradient id="kitchenTone" x1="0" y1="0" x2="1" y2="1">
      <stop offset="0" stop-color="#dcdcdc"/>
      <stop offset="0.6" stop-color="#bdbfc1"/>
      <stop offset="1" stop-color="#5d5f63"/>
    </linearGradient>
    <linearGradient id="bathTone" x1="0" y1="0" x2="1" y2="1">
      <stop offset="0" stop-color="#e6e7e8"/>
      <stop offset="0.6" stop-color="#cfd0d2"/>
      <stop offset="1" stop-color="#9a9c9f"/>
    </linearGradient>
  </defs>

  <!-- pocket flaps -->
  <polygon points="76,744 18,779 18,950 76,985" fill="url(#flapFade)"/>
  <polygon points="1106,744 1164,779 1164,950 1106,985" fill="url(#flapFade)"/>

  <!-- pockets -->
  <polygon points="76,744 586,744 557,985 76,985" fill="url(#blueFade)"/>
  <polygon points="595,744 1106,744 1106,985 625,985" fill="url(#blueFade)"/>

  <!-- back cover -->
  <g class="back-cover">
    <rect x="76" y="56" width="515" height="687" fill="url(#blueFade)"/>
    <text class="back-name" x="333" y="628" text-anchor="middle">Hearth &amp; Tile Crafters</text>
    <text class="address" x="333" y="694" text-anchor="middle">728 NW Folley Lane Suite #217 Marlow Springs, Ohio 50388</text>

    <g class="contact-row">
      <path class="icon-fill" d="M173,705 c1,-1 2,-1 3,0 l1.5,2 c0.5,1 0,2 -1,2.5 c0.5,2 2,3.5 4,4 c0.5,-1 1.5,-1.5 2.5,-1 l2,1.5 c1,1 1,2 0,3 c-1,1 -3,1.5 -5,0.5 c-3,-1.5 -6,-4.5 -7.5,-7.5 c-1,-2 -0.5,-4 0.5,-5z"/>
      <text class="contact" x="193" y="715">555-472-8093</text>

      <rect class="icon" x="258" y="707.5" width="10.5" height="7.5"/>
      <path class="icon" d="M258,707.5 l5.25,4 l5.25,-4"/>
      <text class="contact" x="273" y="715">htcrafterspro@mailvane.net</text>

      <circle class="icon" cx="408" cy="711.5" r="6"/>
      <ellipse class="icon" cx="408" cy="711.5" rx="2.6" ry="6"/>
      <line class="icon" x1="402" y1="711.5" x2="414" y2="711.5"/>
      <text class="contact" x="421" y="715">www.hearthtilecrafters.net</text>
    </g>
  </g>

  <!-- spine fold -->
  <line class="fold" x1="591" y1="56" x2="591" y2="743"/>

  <!-- front cover -->
  <g class="front-cover">
    <rect class="paper" x="591" y="56" width="515" height="688"/>
    <polygon points="880,56 1106,56 1106,371 878,371 772,207" fill="url(#blueFade)"/>
    <polygon class="photo-kitchen" role="img" aria-label="Photo of a remodeled white kitchen with marble island and pendant lights" points="592,210 769,210 873,371 770,582 592,582"/>
    <polygon class="photo-bath" role="img" aria-label="Photo of a remodeled white-tiled bathroom with tub, vanity and window" points="878,380 1104,380 1104,744 873,744 764,585"/>
    <polygon points="592,586 761,586 867,744 592,744" fill="url(#blueFade)"/>

    <rect class="brand-mark" x="609" y="88" width="34" height="48"/>
    <text class="brand-name" x="652" y="108">Hearth &amp; Tile</text>
    <text class="brand-name" x="652" y="130">Crafters</text>

    <text class="web" x="650" y="713">www.hearthtilecrafters.net</text>
  </g>
</svg>
</body>
</html>
```